The Duchess of Nestwares is an online store specialising in all things for the home Bathroom, Kitchen,

I need a business card designed that is professional and elegant, yet not conservative. We will be wanting to brand the entire business and will have videos made where we will be interacting with the product, testing the products and basically creating an online interactive community for all those people interested in all things to do with the Home and the activities that take place in and around the home.

Target Market(s)

30-65yr old Men and Women who LOVE their Home and see it as their primary place of Happiness, their sanctuary!

Industry/Entity Type

Business

Contact Information for Business Card

www.duchessofnestwares.example The Duchess Of Nestwares-PO Box 58391, Mt Ferndale, Auckland. NEW ZEALAND. info@duchessofnestwares.example
Love your Home! Lorraine Becker-Duponte

Font styles to use
Decorative
Script

Colors
9bcb3b
33b8a4
85cae6
b7a5cd
eda3c7
e667a6
d2a4cc
fdf9cf
fee18a

Requirements
Must have
• Attractive colours. Must feel Elegant, yet simple. A font that is rounded without sharp edges. Organic feel to the card, something raw with texture.
Nice to have
• I like the logo deign that I gave in the photos, something feminine, but fun.
Should not have
• I dont like sharp edges, or linear design. I like organic, flowing, fractal type design. Something that looks beautiful in form when you look at it.

```html
<!DOCTYPE html>
<html lang="en">
<head>
<meta charset="utf-8">
<title>The Duchess of Nestwares – Business Card</title>
<link rel="stylesheet" href="https://fonts.googleapis.com/css2?family=Fondamento&family=Questrial&display=swap">
<style>
  :root {
    --page: #ffffff;
    --card-cream: #f8e8d6;
    --card-edge: #fbe9d8;
    --gold-dark: #a87c2a;
    --gold-mid: #c99a32;
    --gold-light: #e0bb3a;
    --teal: #3ec0ad;
    --teal-deep: #14a68e;
  }
  * { margin: 0; padding: 0; box-sizing: border-box; }
  html, body {
    width: 1200px; height: 741px; overflow: hidden; background: var(--page);
  }
  .card {
    position: relative; width: 1200px; height: 741px;
  }
  .card-shape { position: absolute; inset: 0; }
  .brand {
    position: absolute; left: 113px; top: 108px;
    display: flex; align-items: center; gap: 22px;
  }
  .brand-name {
    font-family: "Questrial", sans-serif;
    font-size: 62px; line-height: 1.08; color: var(--teal);
    letter-spacing: 1px;
  }
  .brand-dot {
    width: 46px; height: 46px; border-radius: 50%;
    background: linear-gradient(135deg, var(--gold-light), var(--gold-dark));
  }
  .holder-name {
    position: absolute; left: 110px; top: 392px;
    font-family: "Fondamento", cursive;
    font-size: 50px; line-height: 1;
    background: linear-gradient(90deg, var(--gold-dark), var(--gold-light) 55%, var(--gold-dark));
    -webkit-background-clip: text; background-clip: text; color: transparent;
  }
  .contact {
    position: absolute; left: 156px; top: 472px;
    font-family: "Questrial", sans-serif; font-size: 29px;
    line-height: 39px; color: var(--teal);
    list-style: none;
  }
  .contact .deep { color: var(--teal-deep); }
  .contact-icon { position: absolute; left: 104px; }
  .social {
    position: absolute; left: 913px; top: 605px;
    display: flex; gap: 20px;
  }
  .social span {
    width: 50px; height: 50px; border-radius: 50%;
    background: radial-gradient(circle at 35% 30%, var(--gold-light), var(--gold-dark));
  }
</style>
</head>
<body>
<div class="card">
  <svg class="card-shape" width="1200" height="741" viewBox="0 0 1200 741">
    <defs>
      <linearGradient id="gold-frame" x1="0" y1="0" x2="1" y2="0">
        <stop offset="0" stop-color="#a87c2a"/>
        <stop offset="0.3" stop-color="#e0bb3a"/>
        <stop offset="0.55" stop-color="#a87c2a"/>
        <stop offset="0.8" stop-color="#dcae3c"/>
        <stop offset="1" stop-color="#a87c2a"/>
      </linearGradient>
    </defs>
    <rect x="16" y="16" width="1168" height="706" rx="48" fill="var(--card-edge)"/>
    <rect x="54" y="48" width="1092" height="642" rx="40" fill="var(--card-cream)" stroke="url(#gold-frame)" stroke-width="10"/>
  </svg>

  <div class="brand">
    <div class="brand-name">The Duchess<br>of Nestwares</div>
    <div class="brand-dot"></div>
  </div>

  <div class="holder-name">Lorraine Becker-Duponte</div>

  <ul class="contact">
    <li>The Duchess Of Nestwares</li>
    <li>PO Box 58391, Mt Ferndale</li>
    <li class="deep">Auckland. NEW ZEALAND.</li>
    <li>www.duchessofnestwares.example</li>
    <li class="deep">info@duchessofnestwares.example</li>
  </ul>

  <svg class="contact-icon icon-pin" style="top:512px" width="34" height="34" viewBox="0 0 34 34" aria-hidden="true">
    <path d="M17 3a8 8 0 0 0-8 8c0 6 8 14 8 14s8-8 8-14a8 8 0 0 0-8-8z" fill="none" stroke="var(--gold-mid)" stroke-width="3"/>
    <circle cx="17" cy="11" r="3" fill="var(--gold-mid)"/>
    <ellipse cx="17" cy="28" rx="13" ry="3.5" fill="none" stroke="var(--gold-mid)" stroke-width="2.5"/>
  </svg>
  <svg class="contact-icon icon-globe" style="top:592px" width="34" height="34" viewBox="0 0 34 34" aria-hidden="true">
    <g fill="none" stroke="var(--gold-mid)" stroke-width="2.5">
      <circle cx="17" cy="17" r="13"/>
      <ellipse cx="17" cy="17" rx="6" ry="13"/>
      <line x1="4" y1="17" x2="30" y2="17"/>
      <line x1="6" y1="10" x2="28" y2="10"/>
      <line x1="6" y1="24" x2="28" y2="24"/>
    </g>
  </svg>
  <svg class="contact-icon icon-mail" style="top:630px" width="34" height="34" viewBox="0 0 34 34" aria-hidden="true">
    <rect x="3" y="8" width="28" height="20" rx="2" fill="var(--gold-mid)"/>
    <path d="M3 10l14 10 14-10" fill="none" stroke="var(--card-cream)" stroke-width="2.5"/>
  </svg>

  <div class="social" aria-label="Social media links">
    <span></span><span></span><span></span>
  </div>
</div>
</body>
</html>
```